Fontenot Bayou Grillhouse (Owners Card)

Need a classy, but modern business card. I have included a promotional card for Fontenot Bayou Grillhouse. I need one for myself (the owner) that is more professional.

Target Market(s)

General Public

Industry/Entity Type

Food service

Contact Information for Business Card

Name, business address, phone number, email, logo

Font styles to use
Serif
Sans Serif
Decorative
Script

Requirements
Must have
• My name (Darvel Pruitt), business address (327 Oakmere Street), phone number (510) 493-2615, email (Dpruittkr4@mailvane.example. On the back of the card: Psalms 27 1 The LORD is my light and my salvation— whom shall I fear? The LORD is the stronghold of my life— of whom shall I be afraid? 2 When the wicked advance against me to devour me, it is my enemies and my foes who will stumble and fall. 3 Though an army besiege me, my heart will not fear; though war break out against me, even then I will be confident.
Nice to have
• Something that’s bold, but modern and professional.

```html
<!DOCTYPE html>
<html lang="en">
<head>
<meta charset="utf-8">
<title>Fontenot Bayou Grillhouse – Owner Business Card</title>
<link href="https://fonts.googleapis.com/css2?family=Outfit:wght@400;600;700&family=Source+Sans+3:wght@400;600&display=swap" rel="stylesheet">
<style>
  :root {
    --page: #eef0f1;
    --card-white: #ffffff;
    --ink: #111111;
    --line: #1a1a1a;
    --sketch-tone: #efefef;
    --back-center: #3d3d3d;
    --back-edge: #050505;
    --back-text: #ffffff;
    --back-mark: rgba(255,255,255,0.06);
  }
  * { margin: 0; padding: 0; box-sizing: border-box; }
  html, body { width: 1200px; height: 1200px; overflow: hidden; }
  body { background: var(--page); position: relative; }
  .card {
    position: absolute; left: 248px; width: 703px; height: 401px; overflow: hidden;
  }
  .card-front { top: 150px; background: var(--card-white); }
  .card-back {
    top: 635px;
    background: radial-gradient(ellipse at 45% 45%, var(--back-center) 0%, #1b1b1b 55%, var(--back-edge) 100%);
    color: var(--back-text);
    font-family: "Source Sans 3", sans-serif;
  }
  .owner-name {
    position: absolute; left: 59px; top: 88px;
    font-family: "Outfit", sans-serif; font-weight: 700;
    font-size: 27px; letter-spacing: 0.5px; color: var(--ink);
  }
  .contact-row {
    position: absolute; left: 57px; height: 34px;
    display: flex; align-items: center; gap: 12px;
    font-family: "Outfit", sans-serif; font-weight: 400;
    font-size: 19px; color: var(--ink); white-space: nowrap;
  }
  .contact-row svg { width: 32px; height: 32px; flex: none; }
  .row-address { top: 183px; }
  .row-phone { top: 247px; }
  .row-email { top: 311px; font-size: 16.5px; letter-spacing: -0.1px; }
  .divider {
    position: absolute; left: 382px; top: 47px;
    width: 2px; height: 307px; background: var(--line);
  }
  .brand-name {
    position: absolute; left: 408px; top: 160px; width: 220px;
    text-align: center;
    font-family: "Outfit", sans-serif; font-weight: 700;
    font-size: 25px; line-height: 1.15; color: var(--ink);
    text-transform: uppercase;
  }
  .sketch { position: absolute; background: var(--sketch-tone); border-radius: 40px; }
  .sketch-top { left: 395px; top: -20px; width: 115px; height: 85px; }
  .sketch-right { left: 600px; top: 90px; width: 120px; height: 70px; }
  .sketch-bottom { left: 512px; top: 300px; width: 95px; height: 120px; }
  .psalm-title {
    position: absolute; left: 0; right: 0; top: 22px;
    text-align: center; font-weight: 600; font-size: 44px;
    text-decoration: underline; text-underline-offset: 8px; text-decoration-thickness: 2px;
  }
  .back-mark {
    position: absolute; left: 200px; top: 150px; width: 300px;
    text-align: center;
    font-family: "Outfit", sans-serif; font-weight: 700;
    font-size: 34px; line-height: 1.1; color: var(--back-mark); text-transform: uppercase;
  }
  .verse-line { position: absolute; font-size: 16.5px; white-space: nowrap; }
  .verse-line.lead { left: 48px; }
  .verse-line.trail { right: 44px; }
</style>
</head>
<body>
<section class="card card-front">
  <h1 class="owner-name">DARVEL PRUITT</h1>

  <div class="contact-row row-address">
    <svg viewBox="0 0 32 32" aria-hidden="true"><circle cx="16" cy="16" r="16" fill="#111"/><path d="M16 7a6 6 0 0 0-6 6c0 4.5 6 12 6 12s6-7.5 6-12a6 6 0 0 0-6-6z" fill="#fff"/><circle cx="16" cy="13" r="2.3" fill="#111"/></svg>
    <span>327 Oakmere Street</span>
  </div>
  <div class="contact-row row-phone">
    <svg viewBox="0 0 32 32" aria-hidden="true"><circle cx="16" cy="16" r="16" fill="#111"/><path d="M11 8.5l3 3.5-1.8 2.2c1.2 2.4 3.2 4.4 5.6 5.6l2.2-1.8 3.5 3-2 3c-6.5-.8-11.7-6-12.5-12.5z" fill="#fff"/></svg>
    <span>(510) 493-2615</span>
  </div>
  <div class="contact-row row-email">
    <svg viewBox="0 0 32 32" aria-hidden="true"><circle cx="16" cy="16" r="16" fill="#111"/><path d="M9 22V11l7 6 7-6v11h-3v-5l-4 3.4-4-3.4v5z" fill="#fff"/></svg>
    <span>Dpruittkr4@mailvane.example</span>
  </div>

  <div class="divider"></div>

  <div class="sketch sketch-top" role="img" aria-label="Line sketch of a cut of meat"></div>
  <div class="sketch sketch-right" role="img" aria-label="Line sketch of a cut of meat"></div>
  <div class="sketch sketch-bottom" role="img" aria-label="Line sketch of a cut of meat"></div>

  <p class="brand-name">Fontenot Bayou Grillhouse</p>
</section>

<section class="card card-back">
  <p class="back-mark">Fontenot Bayou Grillhouse</p>
  <h2 class="psalm-title">Psalms 27</h2>
  <p class="verse-line lead" style="top:107px">The LORD is my light and my salvation— whom shall I fear?</p>
  <p class="verse-line trail" style="top:138px">The LORD is the stronghold of my life— of whom shall I be afraid?</p>
  <p class="verse-line lead" style="top:187px">When the wicked advance against me to devour me, it is my enemies</p>
  <p class="verse-line trail" style="top:217px">and my foes who will stumble and fall.</p>
  <p class="verse-line lead" style="top:265px">Though an army besiege me, my heart will not fear; though war break</p>
  <p class="verse-line trail" style="top:294px">out against me, even then I will be confident.</p>
</section>
</body>
</html>
```